Bref créative
Logo for coaching business
Bus card design, stationary/letterhead, envelopes
Professional
Gerald Pinsky
International Author - Coach - Mentor
20583 W. Marigold Ave. #215-347
Scottsdale, AZ 85917
Gerald@brightkestrelcoaching.example
www.BrightKestrelCoaching.example
Need additional bus. card layout for-
Tom Ridgely, MMAC
Life Coach - Counselor
Tom@brightkestrelcoaching.example

```html
<!DOCTYPE html>
<html lang="en">
<head>
<meta charset="utf-8">
<title>Bright Kestrel Coaching – Business Card</title>
<link rel="stylesheet" href="https://fonts.googleapis.com/css2?family=Cinzel:wght@400;600&family=Lato:wght@400&display=swap">
<style>
  :root {
    --backdrop: #e9e9ec;
    --card: #ffffff;
    --ink: #3b3b44;
    --ink-soft: #6d6d78;
    --blue: #1f6fb8;
    --blue-deep: #1b4f93;
    --purple: #8e1f7c;
    --green: #2f9a3a;
    --serif: "Cinzel", "Trajan Pro", serif;
  }
  * { box-sizing: border-box; margin: 0; padding: 0; }
  html, body { width: 1200px; height: 864px; overflow: hidden; }
  body { background: var(--backdrop); position: relative; font-family: var(--serif); color: var(--ink); }

  .card {
    position: absolute; width: 560px; height: 320px; left: 320px;
    background: var(--card); border-radius: 16px; overflow: hidden;
    box-shadow: 0 6px 18px rgba(0,0,0,.18);
  }
  .card--front { top: 64px; }
  .card--back { top: 464px; }

  /* front */
  .front-brand {
    position: absolute; top: 104px; left: 0; width: 100%;
    display: flex; align-items: center; justify-content: center; gap: 14px;
  }
  .brand-dot { width: 44px; height: 44px; border-radius: 50%; background: var(--blue); }
  .brand-name { font-size: 26px; font-weight: 600; color: var(--ink); letter-spacing: .04em; }
  .front-web {
    position: absolute; top: 196px; width: 100%; text-align: center;
    font-size: 11px; letter-spacing: .32em; color: var(--ink-soft);
  }

  /* back */
  .waves { position: absolute; inset: 0; }
  .back-brand { position: absolute; top: 34px; left: 34px; display: flex; align-items: center; gap: 14px; }
  .back-brand .brand-dot { width: 40px; height: 40px; }
  .back-brand .brand-name { font-size: 22px; }
  .tagline {
    position: absolute; top: 80px; left: 88px;
    font-size: 8.5px; letter-spacing: .08em; color: var(--ink-soft);
  }
  .tagline .t-blue { color: var(--blue); }
  .tagline .t-purple { color: var(--purple); }
  .tagline .t-green { color: var(--green); }

  .person { position: absolute; left: 44px; top: 200px; }
  .person-name { font-size: 15px; color: var(--purple); letter-spacing: .04em; }
  .person-role { font-size: 8.5px; color: var(--ink-soft); letter-spacing: .06em; line-height: 1.5; margin-top: 3px; }

  .contact { position: absolute; top: 112px; left: 296px; list-style: none; }
  .contact li { display: flex; align-items: center; gap: 8px; font-size: 8.5px; color: var(--ink); letter-spacing: .04em; height: 17px; }
  .contact svg { width: 12px; height: 12px; flex: none; }
</style>
</head>
<body>

<section class="card card--front" aria-label="Card front">
  <div class="front-brand">
    <span class="brand-dot"></span>
    <span class="brand-name">Bright Kestrel Coaching</span>
  </div>
  <p class="front-web">WWW.BRIGHTKESTRELCOACHING.EXAMPLE</p>
</section>

<section class="card card--back" aria-label="Card back">
  <svg class="waves" viewBox="0 0 560 320" preserveAspectRatio="none" aria-hidden="true">
    <defs>
      <linearGradient id="blue-sweep" x1="0" y1="0" x2="1" y2="1">
        <stop offset="0" stop-color="var(--blue)"/>
        <stop offset="1" stop-color="var(--blue-deep)"/>
      </linearGradient>
    </defs>
    <path d="M0,258 C150,300 330,312 560,262 L560,320 L0,320 Z" fill="url(#blue-sweep)"/>
    <path d="M150,320 C330,306 470,272 560,218 L560,320 Z" fill="#ffffff"/>
    <path d="M200,320 C360,308 480,280 560,232 L560,320 Z" fill="var(--purple)"/>
  </svg>

  <div class="back-brand">
    <span class="brand-dot"></span>
    <span class="brand-name">Bright Kestrel Coaching</span>
  </div>
  <p class="tagline">
    <span class="t-blue">NEW CHALLENGES</span> · <span class="t-purple">NEW ATTITUDE</span> · <span class="t-green">NEW LIFE</span>
  </p>

  <div class="person">
    <p class="person-name">Gerald Pinsky</p>
    <p class="person-role">INTERNATIONAL AUTHOR<br>COACH · MENTOR</p>
  </div>

  <ul class="contact">
    <li>
      <svg viewBox="0 0 12 12"><circle cx="6" cy="6" r="6" fill="var(--ink-soft)"/><path d="M6 2.6a2 2 0 0 0-2 2c0 1.6 2 4.2 2 4.2s2-2.6 2-4.2a2 2 0 0 0-2-2z" fill="#fff"/></svg>
      20583 W. Marigold Ave. #215-347
    </li>
    <li>
      <svg viewBox="0 0 12 12"><circle cx="6" cy="6" r="6" fill="var(--ink-soft)"/></svg>
      Scottsdale, AZ 85917
    </li>
    <li>
      <svg viewBox="0 0 12 12"><circle cx="6" cy="6" r="6" fill="var(--ink-soft)"/><path d="M4 3h1.3l.6 1.6-.8.6a4 4 0 0 0 1.7 1.7l.6-.8L9 6.7V8a1 1 0 0 1-1 1A5 5 0 0 1 3 4a1 1 0 0 1 1-1z" fill="#fff"/></svg>
      480-555-0172
    </li>
    <li>
      <svg viewBox="0 0 12 12"><circle cx="6" cy="6" r="6" fill="var(--ink-soft)"/><rect x="3" y="4" width="6" height="4" fill="#fff"/><path d="M3 4l3 2.2L9 4" stroke="var(--ink-soft)" stroke-width=".7" fill="none"/></svg>
      Gerald@brightkestrelcoaching.example
    </li>
    <li>
      <svg viewBox="0 0 12 12"><circle cx="6" cy="6" r="6" fill="var(--ink-soft)"/><circle cx="6" cy="6" r="3" fill="none" stroke="#fff" stroke-width=".8"/><path d="M3 6h6M6 3v6" stroke="#fff" stroke-width=".6"/></svg>
      www.BrightKestrelCoaching.example
    </li>
  </ul>
</section>

</body>
</html>
```